Chocolate company needing sticker for products

I have a small chocolate company Willow Bend Sweets in Austin Texas. I make all vegan, gluten free, organic, faire trade chocolate that tastes amazing! It is allergy friendly approvable by all ages. I want to have a great sticker that i can put on our boxes and bags. I am using a lot of natural craft color and brown. I am open to color options possibly for different flavors. I want the packaging to reflect the basis of my company. It is all handmade by me but i don't want it to have to much of a crafty look to it. I have attached the logo designs I have. it the sticker can have som of the bullet points about the company that would be great. But it needs to say Locally Made in Austin Texas. it also has to have the company address.
418 West Cobbler Ridge Rd #207 Austin Tx 78745. These things are required by the state for food regulations. I want something that looks great and I can be really proud to put on my product! Thanks so much for all of your help in advance. Dot

I also need some other information added to the sticker. Website which is willowbendsweetsatx.com 

Phone number 512.368.4175. Instagram willowbendsweets. Thanks for your hard work! 

Industry/Entity Type

Chocolate Company

Requirements
Must have
• The logo is added at the bottom as well as designs I like I want to have a professional look but it to be approvable by all consumers. I will gig feed back as i see what designs come through. This will probably fold out into a multi design project so i will be looking for assistance on other areas of this as well. Thanks

```html
<!DOCTYPE html>
<html lang="en">
<head>
<meta charset="utf-8">
<title>Willow Bend Sweets — Product Sticker</title>
<link rel="stylesheet" href="https://fonts.googleapis.com/css2?family=Playfair+Display:wght@700&family=Oswald:wght@500&family=Arimo&family=Libre+Baskerville:wght@700&display=swap">
<style>
  :root {
    --page: #3a2219;
    --paper: #e8e2d5;
    --paper-shade: #dcd4c3;
    --cocoa: #4a2e24;
    --cocoa-dark: #3d251c;
    --berry: #c8373a;
    --berry-dark: #9e2a2d;
    --cream: #fbf7ee;
    --ink: #3b2418;
  }
  html, body {
    margin: 0;
    width: 1200px;
    height: 1000px;
    overflow: hidden;
    background: var(--page);
  }
  .canvas {
    position: relative;
    width: 1200px;
    height: 1000px;
  }
  .sticker {
    position: absolute;
    left: 132px;
    top: 105px;
    width: 936px;
    height: 788px;
    background: radial-gradient(ellipse at 50% 40%, var(--paper) 55%, var(--paper-shade) 100%);
    box-shadow: 0 10px 30px rgba(0,0,0,.35);
  }
  .sticker-art {
    position: absolute;
    left: 0;
    top: 0;
  }
  .brand-line {
    font-family: "Playfair Display", serif;
    font-weight: 700;
    fill: var(--cream);
  }
  .brand-connector {
    font-family: "Oswald", sans-serif;
    font-weight: 500;
    fill: var(--cream);
  }
  .ribbon-text {
    font-family: "Libre Baskerville", serif;
    font-weight: 700;
    fill: var(--cream);
  }
  .contact {
    position: absolute;
    left: 0;
    right: 0;
    top: 680px;
    margin: 0;
    text-align: center;
    font-family: "Arimo", sans-serif;
    font-size: 26px;
    line-height: 40px;
    color: var(--ink);
  }
</style>
</head>
<body>
<main class="canvas">
  <section class="sticker">
    <svg class="sticker-art" width="936" height="788" viewBox="0 0 936 788">
      <!-- Main label plaque -->
      <g class="label-plaque" transform="translate(70,100) rotate(-5 380 235)">
        <path class="plaque-border" fill="var(--berry)"
          d="M 90,30 C 250,0 510,0 670,30 Q 690,60 730,60 C 760,160 760,310 730,410 Q 690,410 670,440 C 510,470 250,470 90,440 Q 70,410 30,410 C 0,310 0,160 30,60 Q 70,60 90,30 Z"/>
        <path class="plaque-body" fill="var(--cocoa)" transform="translate(15.2,9.4) scale(0.96)"
          d="M 90,30 C 250,0 510,0 670,30 Q 690,60 730,60 C 760,160 760,310 730,410 Q 690,410 670,440 C 510,470 250,470 90,440 Q 70,410 30,410 C 0,310 0,160 30,60 Q 70,60 90,30 Z"/>
        <path class="plaque-stitch" fill="none" stroke="var(--cream)" stroke-width="3.5" stroke-linecap="round" stroke-dasharray="0 9"
          d="M 110,62 C 260,38 500,38 650,62 M 110,408 C 260,432 500,432 650,408 M 62,110 C 44,190 44,280 62,360 M 698,110 C 716,190 716,280 698,360"/>
        <line class="rule-top" x1="150" y1="92" x2="610" y2="92" stroke="var(--cream)" stroke-width="3.5" stroke-linecap="round" stroke-dasharray="0 9"/>
        <line class="rule-bottom" x1="150" y1="400" x2="610" y2="400" stroke="var(--cream)" stroke-width="3.5" stroke-linecap="round" stroke-dasharray="0 9"/>

        <ellipse class="cocoa-pod-left" cx="95" cy="238" rx="48" ry="30" fill="#6b5248" role="img" aria-label="Cocoa pod and leaves illustration"/>
        <ellipse class="cocoa-pod-right" cx="665" cy="238" rx="48" ry="30" fill="#6b5248" role="img" aria-label="Cocoa pod and leaves illustration"/>

        <text class="brand-line" x="380" y="190" font-size="108" text-anchor="middle" textLength="470" lengthAdjust="spacingAndGlyphs">WILLOW</text>
        <circle cx="290" cy="250" r="4" fill="var(--cream)"/>
        <circle cx="470" cy="250" r="4" fill="var(--cream)"/>
        <text class="brand-connector" x="380" y="268" font-size="52" text-anchor="middle">BEND</text>
        <text class="brand-line" x="380" y="378" font-size="108" text-anchor="middle" textLength="470" lengthAdjust="spacingAndGlyphs">SWEETS</text>
      </g>

      <!-- Locally made ribbon -->
      <g class="local-ribbon" transform="rotate(-4 790 400)">
        <path d="M 752,560 L 792,560 L 808,610 L 790,596 L 772,612 Z" fill="var(--berry-dark)"/>
        <rect x="748" y="290" width="84" height="280" fill="var(--berry)"/>
        <rect x="754" y="296" width="72" height="268" fill="none" stroke="var(--cream)" stroke-width="1.5"/>
        <text class="ribbon-text" transform="translate(786 545) rotate(-90)" font-size="19" textLength="230" lengthAdjust="spacingAndGlyphs">LOCALLY MADE IN</text>
        <text class="ribbon-text" transform="translate(812 545) rotate(-90)" font-size="22" textLength="230" lengthAdjust="spacingAndGlyphs">AUSTIN TEXAS</text>
      </g>

      <!-- Certification badge placeholder -->
      <g class="local-badge">
        <circle cx="780" cy="200" r="96" fill="var(--berry)"/>
        <circle cx="780" cy="200" r="82" fill="var(--cream)" stroke="var(--cocoa-dark)" stroke-width="3"/>
      </g>
    </svg>

    <p class="contact">
      418 West Cobbler Ridge Rd #207 Austin Tx 78745<br>
      Phone: 512.368.4175, www.willowbendsweetsatx.com
    </p>
  </section>
</main>
</body>
</html>
```